Pemby Icewear Brochure

tagline_
- skatewear for everywhere

Brochure to showcase our clothing line/products
Sending to various stores around the country for them to carry the line.
Fun, attention getting brochure.
Template that we can change per season for different clothing/new products.
I've included my logo and can provide all photo's of current clothing that will need to be included in the brochure.

PLEASE USE IMAGE IMG_1454.JPG FOR COVER OF BROCHURE

Target Market(s)

Figure Skaters around the world. Age range anywhere between 4yrs old to an adult skater. Ice Skaters and fan's of ice skating. Female

Industry/Entity Type

Clothing

Requirements
Must have
• All photo's of clothing products/ descriptions

Must have product description next to each photo.
Velvet Comet etc.

Mission statement:
At Pemby our goal is to provide you cutting edge, super stylish, high quality apparel that’s wearable on the ice or out on the town.

Contact information for Brochure.

Contact us at:
Pemby Icewear
PO Box 4073
Sun Valley, Idaho 83353
Phone: 208-555-0148
Email: info@pembyicewear.example
www.pembyicewear.example
www.facebook.example/pembyicewear
www.twitter.example/pembyicewear

```html
<!DOCTYPE html>
<html lang="en">
<head>
<meta charset="utf-8">
<title>Pemby Icewear – Tops</title>
<link href="https://fonts.googleapis.com/css2?family=Marcellus&family=Montserrat:wght@400;600;700&display=swap" rel="stylesheet">
<style>
  :root{
    --stage:#000;
    --paper:#fff;
    --fuchsia:#e6197f;
    --blush:#f0d4e0;
    --blush-deep:#e8c2d4;
    --sky:#a9c4e6;
    --swirl:#2f4d66;
    --ink:#555;
    --rule:#777;
    --band:#8a8a8a;
  }
  *{margin:0;padding:0;box-sizing:border-box}
  html,body{width:1200px;height:900px;overflow:hidden;background:var(--stage)}
  .spread{position:absolute;left:28px;top:250px;width:1144px;height:402px;display:flex;gap:3px}
  .page{position:relative;width:570px;height:402px;background:var(--paper);overflow:hidden;font-family:"Montserrat",sans-serif}
  .page-bg{position:absolute;inset:0}
  .section-tab{position:absolute;top:17px;font-size:8px;letter-spacing:.5px;color:var(--ink);font-weight:600}
  .section-tab b{color:var(--fuchsia)}
  .page--left .section-tab{left:19px}
  .page--right .section-tab{right:19px}
  .product-title{position:absolute;z-index:2;font-family:"Marcellus",serif;color:var(--fuchsia);font-size:25px;line-height:27px;font-weight:400;white-space:nowrap}
  .product-copy{position:absolute;z-index:2;color:var(--ink);font-size:10.5px;line-height:13px;white-space:nowrap}
  .photo{position:absolute;border-radius:90px 90px 0 0}
  .price{position:absolute;width:92px;height:86px}
  .price-label{position:absolute;inset:0;display:flex;flex-direction:column;align-items:center;justify-content:center;color:#fff;font-weight:700;line-height:1;transform:rotate(-12deg);padding-bottom:8px}
  .price-label small{font-size:9px}
  .price-label span{font-size:20px}
  .size-chart{position:absolute;width:108px;background:#fff;border-radius:5px;padding:3px;box-shadow:0 0 0 1px #eee;font-size:7.4px;color:#333}
  .size-chart table{width:100%;border-collapse:collapse}
  .size-chart td,.size-chart th{border:1px solid var(--rule);padding:0 2px;height:11.5px;text-align:left;font-weight:400}
  .chart-head th{background:var(--fuchsia);color:#fff;font-weight:600;border-color:var(--fuchsia)}
  .chart-group td{background:var(--band);color:#fff;border-color:var(--band)}
  .size-code{background:var(--fuchsia);color:#fff;font-weight:700;width:10px}
</style>
</head>
<body>
<main class="spread">

  <section class="page page--left">
    <svg class="page-bg" width="570" height="402" viewBox="0 0 570 402">
      <path d="M0 0H250C200 40 160 80 120 110 80 140 40 160 0 170Z" fill="var(--blush)"/>
      <path d="M180 0H330C310 15 270 20 230 12 205 8 190 4 180 0Z" fill="var(--sky)"/>
      <path d="M520 0H570V40C550 30 530 15 520 0Z" fill="var(--blush)"/>
      <path d="M350 402C360 330 400 280 460 270 520 262 555 220 570 200V402Z" fill="var(--blush)"/>
      <path role="img" aria-label="Decorative blue swirl pattern band"
        d="M60 402C45 350 65 310 105 300 140 290 150 250 155 200 160 150 185 112 230 110 280 108 330 128 380 130 430 132 460 115 490 85 520 55 545 45 570 40V250C540 262 505 262 480 240 455 215 425 215 405 240 380 268 340 262 315 235 290 208 262 215 250 255 238 310 232 360 215 402Z"
        fill="var(--swirl)"/>
      <path d="M375 160C400 130 445 140 460 175 475 215 440 250 405 238 375 228 358 190 375 160Z" fill="var(--blush-deep)" opacity=".7"/>
    </svg>
    <div class="section-tab">TOPS <b>&gt;</b></div>
    <h2 class="product-title" style="left:266px;top:26px">iLOVE GLIDING</h2>
    <p class="product-copy" style="left:266px;top:59px">White Tee<br>100% Cotton<br>Graphic:<br>“I like boys...I heart figure skating”</p>

    <div class="photo" role="img" aria-label="Photo of a young skater wearing the white iLove Gliding tee"
      style="left:88px;top:108px;width:180px;height:294px;background:linear-gradient(180deg,#ecd6a8 0%,#f2dcc8 30%,#fbfbfb 55%,#f4f4f4 100%)"></div>

    <div class="price" style="left:27px;top:92px">
      <svg width="92" height="86" viewBox="0 0 92 86">
        <g transform="rotate(-12 46 43)">
          <path d="M46 82C20 62 2 46 2 27 2 12 13 3 26 3 35 3 42 8 46 15 50 8 57 3 66 3 79 3 90 12 90 27 90 46 72 62 46 82Z" fill="#f6c9de"/>
          <path d="M46 74C24 57 10 44 10 29 10 17 18 10 28 10 36 10 42 14 46 21 50 14 56 10 64 10 74 10 82 17 82 29 82 44 68 57 46 74Z" fill="#f08cbc"/>
          <path d="M46 67C28 53 17 42 17 30 17 21 23 16 30 16 37 16 42 20 46 26 50 20 55 16 62 16 69 16 75 21 75 30 75 42 64 53 46 67Z" fill="var(--fuchsia)"/>
        </g>
      </svg>
      <div class="price-label"><small>US$</small><span>22</span></div>
    </div>

    <div class="size-chart" style="left:309px;top:244px">
      <table>
        <tr class="chart-head"><th colspan="3">SIZE CHART</th></tr>
        <tr class="chart-group"><td colspan="3">Kids</td></tr>
        <tr><td colspan="2">Size</td><td>Chest to Fit</td></tr>
        <tr><td class="size-code">S</td><td>6-8</td><td>23" - 25"</td></tr>
        <tr><td class="size-code">M</td><td>10-12</td><td>25" - 27"</td></tr>
        <tr><td class="size-code">L</td><td>14-16</td><td>27" - 29"</td></tr>
        <tr class="chart-group"><td colspan="3">Adult</td></tr>
        <tr><td class="size-code">S</td><td>0-4</td><td>31" - 33"</td></tr>
        <tr><td class="size-code">M</td><td>4-8</td><td>34" - 36"</td></tr>
        <tr><td class="size-code">L</td><td>8-10</td><td>37" - 39"</td></tr>
      </table>
    </div>
  </section>

  <section class="page page--right">
    <svg class="page-bg" width="570" height="402" viewBox="0 0 570 402">
      <path d="M200 402C210 340 260 300 300 290 340 280 370 300 390 340 400 370 400 390 400 402Z" fill="var(--sky)" opacity=".8"/>
      <path d="M40 402C50 330 120 300 180 310 230 318 240 360 235 402Z" fill="var(--sky)" opacity=".5"/>
      <path d="M230 120C280 100 330 130 330 190 330 240 290 270 250 250 210 230 200 140 230 120Z" fill="var(--blush)"/>
      <path d="M430 230C470 220 530 210 570 220V402H450C420 340 410 260 430 230Z" fill="var(--blush)"/>
      <path role="img" aria-label="Decorative blue swirl pattern band"
        d="M0 0H330C360 20 390 70 400 110 410 140 440 150 470 120 500 90 540 50 570 45V200C540 210 520 240 500 240 470 240 450 200 420 200 390 200 380 160 370 120 360 90 340 65 300 50 260 35 220 30 180 35 130 42 100 70 88 120 76 180 60 230 0 255Z"
        fill="var(--swirl)"/>
    </svg>
    <div class="section-tab"><b>&lt;</b> TOPS</div>
    <h2 class="product-title" style="left:119px;top:76px">SPARKLE<br>HEARTS</h2>
    <p class="product-copy" style="left:120px;top:137px">Ringer Tee with Fuchsia<br>100% Cotton</p>

    <div class="photo" role="img" aria-label="Photo of a teen skater wearing the Sparkle Hearts ringer tee"
      style="left:290px;top:40px;width:280px;height:362px;background:linear-gradient(180deg,#f0dcae 0%,#f3dccb 35%,#fafafa 60%,#f2eef2 100%)"></div>

    <div class="price" style="left:50px;top:244px">
      <svg width="92" height="86" viewBox="0 0 92 86">
        <g transform="rotate(-12 46 43)">
          <path d="M46 82C20 62 2 46 2 27 2 12 13 3 26 3 35 3 42 8 46 15 50 8 57 3 66 3 79 3 90 12 90 27 90 46 72 62 46 82Z" fill="#f6c9de"/>
          <path d="M46 74C24 57 10 44 10 29 10 17 18 10 28 10 36 10 42 14 46 21 50 14 56 10 64 10 74 10 82 17 82 29 82 44 68 57 46 74Z" fill="#f08cbc"/>
          <path d="M46 67C28 53 17 42 17 30 17 21 23 16 30 16 37 16 42 20 46 26 50 20 55 16 62 16 69 16 75 21 75 30 75 42 64 53 46 67Z" fill="var(--fuchsia)"/>
        </g>
      </svg>
      <div class="price-label"><small>US$</small><span>22</span></div>
    </div>

    <div class="size-chart" style="left:161px;top:244px">
      <table>
        <tr class="chart-head"><th colspan="3">SIZE CHART</th></tr>
        <tr class="chart-group"><td colspan="3">Kids</td></tr>
        <tr><td colspan="2">Size</td><td>Chest to Fit</td></tr>
        <tr><td class="size-code">S</td><td>6-8</td><td>23" - 25"</td></tr>
        <tr><td class="size-code">M</td><td>10-12</td><td>25" - 27"</td></tr>
        <tr><td class="size-code">L</td><td>14-16</td><td>27" - 29"</td></tr>
        <tr class="chart-group"><td colspan="3">Adult</td></tr>
        <tr><td class="size-code">S</td><td>0-4</td><td>31" - 33"</td></tr>
        <tr><td class="size-code">M</td><td>4-8</td><td>34" - 36"</td></tr>
        <tr><td class="size-code">L</td><td>8-10</td><td>37" - 39"</td></tr>
      </table>
    </div>
  </section>

</main>
</body>
</html>
```